Book title: Wildflower: The gift of stillness!

This book is called: Wildflower: The gift of stillness!

A guide to understanding the most popular types of coaching and how to find the perfect coach for you.
The coaching industry has exploded over the past few years as the demand for them has increased. With so many different types of coaches it can be intimidating and overwhelming to find the perfect one for you. To further complicate matters, you may experience times in your life when you require multiple coaches. {Book Title} aims to quite the noise and assist you in finding the perfect coach for you. In this book, you will learn more about the different types of coaching as well as meet a hand-picked selection of coaches from the most popular coaching niches. Each featured coach has provided an exercise designed to move you powerfully forward. We encourage you to work through each exercise so you may experience firsthand the power of working with these incredible coaches.

We would like a professional and simple design. See examples included. We would like to see blood orange included in the design, please see color pallets included as well.

Target Market(s)

Corporate professionals wanting to explore the various types of coaching industry

Industry/Entity Type

Coaching - Health, business, spiritual

Font styles to use
Serif

Colors
EE7325
F08F49
F5BC92
FAE3D3
FDF4ED

Requirements
Must have
• Please include book title: Wildflower, Subtitle: The gift of stillness! Name of publishing company: Silver Lantern Publishing, Spaces for 8 author names on the front of the cover- Author Name
Nice to have
• A feminine yet corporate feel.
Should not have
• We don't want it

```html
<!DOCTYPE html>
<html lang="en">
<head>
<meta charset="utf-8">
<title>Wildflower: The gift of stillness!</title>
<link rel="stylesheet" href="https://fonts.googleapis.com/css2?family=Bodoni+Moda:opsz,wght@6..96,400;6..96,500&family=Jost:wght@400&display=swap">
<style>
  :root {
    --blood-orange: #f54c0b;
    --cream: #fae3d3;
  }
  html, body {
    margin: 0;
    padding: 0;
    overflow: hidden;
    background: var(--blood-orange);
  }
  .cover {
    position: relative;
    width: 750px;
    height: 1200px;
    background: var(--blood-orange);
    overflow: hidden;
  }
  .power-lines {
    position: absolute;
    left: 17px;
    top: 17px;
    width: 675px;
    height: 666px;
    background: linear-gradient(180deg, rgba(60, 20, 5, 0.22) 0%, rgba(60, 20, 5, 0.08) 60%, rgba(60, 20, 5, 0) 100%);
  }
  .title {
    position: absolute;
    left: 0;
    top: 0;
    width: 750px;
    height: 820px;
  }
  .title text {
    font-family: "Bodoni Moda", "Playfair Display", serif;
    font-weight: 500;
    font-size: 258px;
    fill: var(--cream);
  }
  .rule {
    position: absolute;
    left: 75px;
    width: 592px;
    height: 3px;
    background: var(--cream);
  }
  .rule--top { top: 827px; }
  .rule--bottom { top: 906px; }
  .subtitle {
    position: absolute;
    left: 55px;
    top: 848px;
    width: 632px;
    margin: 0;
    text-align: center;
    font-family: "Jost", sans-serif;
    font-size: 31px;
    letter-spacing: 0.26em;
    text-transform: uppercase;
    color: var(--cream);
    line-height: 40px;
    white-space: nowrap;
  }
  .authors {
    position: absolute;
    left: 10px;
    top: 1060px;
    width: 730px;
    margin: 0;
    text-align: center;
    font-family: "Jost", sans-serif;
    font-size: 21px;
    line-height: 33px;
    text-transform: uppercase;
    color: var(--cream);
    white-space: nowrap;
  }
  .publisher {
    position: absolute;
    left: 0;
    top: 1165px;
    width: 750px;
    margin: 0;
    text-align: center;
    font-family: "Jost", sans-serif;
    font-size: 13px;
    letter-spacing: 0.3em;
    line-height: 18px;
    text-transform: uppercase;
    color: var(--cream);
  }
</style>
</head>
<body>
  <main class="cover">
    <div class="power-lines" role="img" aria-label="Illustration of two wooden utility poles joined by overhead power lines"></div>

    <svg class="title" viewBox="0 0 750 820" aria-label="Wildflower" role="heading" aria-level="1">
      <text x="50" y="371" textLength="642" lengthAdjust="spacingAndGlyphs">WILD</text>
      <text x="50" y="587" textLength="642" lengthAdjust="spacingAndGlyphs">FLOW</text>
      <text x="375" y="792" text-anchor="middle">ER</text>
    </svg>

    <div class="rule rule--top"></div>
    <p class="subtitle">The gift of stillness!</p>
    <div class="rule rule--bottom"></div>

    <p class="authors">
      Author Name || Author Name || Author Name || Author Name<br>
      Author Name || Author Name || Author Name || Author Name<br>
      Author Name || Author Name
    </p>
    <p class="publisher">Silver Lantern Publishing</p>
  </main>
</body>
</html>
```